Bref créative
KorvaLyne Stationary
Dennis Traven's cards
Professional
Dennis Traven, EdD, LLM, MPA
Owner/Senior Consultant
PO Box 862
587E Harwick Rd
Marrowfield, MN 53418-4471
dtraven@korvalyne-consulting.example
www.korvalyne-consulting.example
Finding clear paths through your learning challenges. Side by side.
KorvaLyne-Consulting, LLC is proud to be a member of:
Gerald K Venn, Venn's consortium
Continental Guild of Learning Advisors and Presenters

```html
<!DOCTYPE html>
<html lang="en">
<head>
<meta charset="utf-8">
<title>KorvaLyne Consulting – Business Card</title>
<link rel="stylesheet" href="https://fonts.googleapis.com/css2?family=Open+Sans:ital,wght@0,400;0,600;0,700;1,400&display=swap">
<style>
  :root {
    --teal: #1f7590;
    --teal-dark: #0e4a5e;
    --teal-light: #3a9ab5;
    --ink: #2e3b44;
    --grey: #6b6f73;
    --card: #ffffff;
    --bg: #e6e7e9;
    --steel-1: #f2f3f4;
    --steel-2: #9da2a7;
  }
  * { margin: 0; padding: 0; box-sizing: border-box; }
  html, body {
    width: 1200px; height: 902px; overflow: hidden;
    background: var(--bg);
    font-family: "Open Sans", Arial, sans-serif;
  }
  .card {
    position: absolute; left: 75px; top: 151px;
    width: 1050px; height: 600px;
    background: var(--card);
    box-shadow: 0 6px 24px rgba(0,0,0,0.18);
  }
  .brand {
    position: absolute; left: 210px; top: 85px;
    display: flex; align-items: center; gap: 20px;
  }
  .brand-dot {
    width: 130px; height: 130px; border-radius: 50%;
    background: var(--teal-dark);
    flex: none;
  }
  .brand-name {
    font-size: 48px; font-weight: 600; color: var(--teal-dark);
    letter-spacing: -0.5px; line-height: 1;
  }
  .brand-llc { font-size: 13px; vertical-align: super; }
  .brand-tagline {
    margin-top: 8px; font-size: 13px; font-style: italic;
    color: var(--grey); letter-spacing: 0.3px;
  }
  .person {
    position: absolute; left: 0; right: 0; top: 290px;
    text-align: center;
  }
  .person-name { font-size: 27px; font-weight: 600; color: var(--teal); }
  .person-title { margin-top: 4px; font-size: 18px; color: var(--grey); }
  .contacts {
    position: absolute; left: 105px; right: 60px; top: 400px;
    font-size: 18px; color: var(--ink);
  }
  .contact-row { display: flex; gap: 22px; margin-bottom: 12px; white-space: nowrap; }
  .contact-item { display: flex; align-items: center; gap: 7px; }
  .contact-item svg { width: 20px; height: 20px; flex: none; }
  .footer-band {
    position: absolute; left: 0; right: 0; top: 498px; height: 56px;
  }
  .steel-bar {
    position: absolute; top: 10px; height: 34px;
    background: linear-gradient(180deg, var(--steel-1), var(--steel-2) 55%, var(--steel-1));
  }
  .steel-bar.left { left: 0; width: 300px; }
  .steel-bar.right { right: 0; width: 240px; }
  .web-tab {
    position: absolute; left: 300px; right: 240px; top: 0; height: 56px;
    background: linear-gradient(180deg, var(--teal-light), var(--teal-dark));
    border-radius: 6px 6px 0 0;
    color: #fff; font-size: 19px; letter-spacing: 2px;
    display: flex; align-items: center; justify-content: center;
  }
</style>
</head>
<body>
  <div class="card">
    <div class="brand">
      <div class="brand-dot"></div>
      <div>
        <div class="brand-name">KorvaLyne-Consulting<span class="brand-llc">,LLC</span></div>
        <div class="brand-tagline">Finding clear paths through your learning challenges. Side by side.</div>
      </div>
    </div>

    <div class="person">
      <div class="person-name">Dennis Traven, EdD, LLM, MPA</div>
      <div class="person-title">Owner/Senior Consultant</div>
    </div>

    <div class="contacts">
      <div class="contact-row">
        <span class="contact-item">
          <svg viewBox="0 0 20 20"><circle cx="10" cy="10" r="10" fill="var(--teal)"/><path d="M10 4a4 4 0 0 0-4 4c0 3 4 8 4 8s4-5 4-8a4 4 0 0 0-4-4z" fill="#fff"/><circle cx="10" cy="8" r="1.5" fill="var(--teal)"/></svg>
          862 587E Harwick Rd Marrowfield, MN 53418-4471
        </span>
        <span class="contact-item">
          <svg viewBox="0 0 20 20"><circle cx="10" cy="10" r="10" fill="var(--teal)"/><path d="M6 5h3l1 3-2 1a8 8 0 0 0 3 3l1-2 3 1v3c-6 0-9-3-9-9z" fill="#fff"/></svg>
          847-555-0142
        </span>
        <span class="contact-item">
          <svg viewBox="0 0 20 20"><circle cx="10" cy="10" r="10" fill="var(--teal)"/><rect x="7" y="4" width="6" height="12" rx="1" fill="#fff"/></svg>
          847-555-0178
        </span>
      </div>
      <div class="contact-row">
        <span class="contact-item">
          <svg viewBox="0 0 20 20"><circle cx="10" cy="10" r="10" fill="var(--teal)"/><path d="M6 5h3l1 3-2 1a8 8 0 0 0 3 3l1-2 3 1v3c-6 0-9-3-9-9z" fill="#fff"/></svg>
          262-555-0119
        </span>
        <span class="contact-item">
          <svg viewBox="0 0 20 20"><circle cx="10" cy="10" r="10" fill="var(--teal)"/><rect x="5" y="6" width="10" height="8" fill="#fff"/><path d="M5 6l5 4 5-4" fill="none" stroke="var(--teal)" stroke-width="1"/></svg>
          dtraven@korvalyne-consulting.example
        </span>
        <span class="contact-item">
          <svg viewBox="0 0 20 20"><circle cx="10" cy="10" r="10" fill="var(--teal)"/><circle cx="10" cy="10" r="5" fill="none" stroke="#fff" stroke-width="1.3"/><path d="M5 10h10M10 5c-2 3-2 7 0 10M10 5c2 3 2 7 0 10" fill="none" stroke="#fff" stroke-width="1"/></svg>
          www.korvalyne-consulting.example
        </span>
      </div>
    </div>

    <div class="footer-band">
      <div class="steel-bar left"></div>
      <div class="web-tab">www.Korvalyne-consulting.example</div>
      <div class="steel-bar right"></div>
    </div>
  </div>
</body>
</html>
```